Dog breeder design card

A card for our dog showing/breeding and companion puppy buyers.
Updates

Project Deadline Extended
Reason: The photo's I provided were not seen by designers because of a glitch or error, so I will need to start them over again in the designs submitted to me. I uploaded and emailed the photo's last night.

Thank you all so much for your lovely designs, I like wquite a few of them. I provided images in my original brief, but these apparently did not become available for you to see. I have emailed my images now, so hopefully you may be able to incorporate them into your designs.

Thank you so much for your time,
kind regards,
Beatrice

I have attached the photo’s that can hopefully be incorporated onto my business card. I don’t mind if the whole images aren’t used, but maybe a soft focus look around the adult dog and in a corner of the card maybe....if that’s possible.

Contact Information for Business Card

Kestamor Bullmastiffs, adored by Gerald and Beatrice Lindqvist.
Cranebrook NSW
0497 358614

Requirements
Nice to have
• Soft focus look to the outline of adult dogs head incorporated into perhaps a corner of the card. Soft focus outline around pups perhaps.
I do really love hot pink and/or purple text if possible.
"Kestamor Bullmastiffs" to be incorporated on the front of card, our details on reverse.
Would prefer a glossy finish rather than matt.

```html
<!DOCTYPE html>
<html lang="en">
<head>
<meta charset="utf-8">
<title>Kestamor Bullmastiffs Card</title>
<link rel="stylesheet" href="https://fonts.googleapis.com/css2?family=Exo+2:wght@600&display=swap">
<style>
  :root {
    --page: #ffffff;
    --frame-red: #c8102e;
    --band-pink: #ad438c;
    --card-purple: #6d2787;
    --wave-purple: #5e1f7b;
    --name-pink: #d55a9b;
    --name-white: #ffffff;
    --url-grey: #cdbfd4;
    --photo-dark: #2e3550;
    --photo-tan: #cfae8e;
  }
  html, body {
    margin: 0;
    padding: 0;
    width: 1200px;
    height: 741px;
    overflow: hidden;
    background: var(--page);
  }
  .canvas {
    position: relative;
    width: 1200px;
    height: 741px;
  }
  .card-art {
    position: absolute;
    inset: 0;
  }
  .puppy-photo {
    position: absolute;
    left: 455px;
    top: 195px;
    width: 262px;
    height: 185px;
    transform: rotate(-10deg);
    background: radial-gradient(ellipse at 50% 45%, var(--photo-tan) 0%, #b99677 38%, var(--photo-dark) 72%);
    box-shadow: 0 0 8px 3px rgba(60, 20, 80, 0.35);
  }
  .kennel-name {
    position: absolute;
    left: 0;
    width: 1246px;
    top: 398px;
    margin: 0;
    text-align: center;
    font-family: "Exo 2", sans-serif;
    font-weight: 600;
    font-size: 47px;
    letter-spacing: 0.5px;
    line-height: 1;
  }
  .kennel-name .first { color: var(--name-pink); }
  .kennel-name .second { color: var(--name-white); }
  .web-address {
    position: absolute;
    left: 0;
    width: 1192px;
    top: 454px;
    margin: 0;
    text-align: center;
    font-family: Arial, Helvetica, sans-serif;
    font-size: 12.5px;
    color: var(--url-grey);
  }
</style>
</head>
<body>
<div class="canvas">
  <svg class="card-art" width="1200" height="741" viewBox="0 0 1200 741" aria-hidden="true">
    <rect class="presentation-frame" x="19" y="19" width="1162" height="703" fill="none" stroke="var(--frame-red)" stroke-width="4"/>
    <rect class="card-base" x="41" y="41" width="1121" height="659" fill="var(--band-pink)"/>
    <path class="top-wave" fill="var(--wave-purple)"
      d="M41 112 C150 108 230 148 330 150 C440 152 520 110 640 108 C760 106 840 140 940 140 C1040 140 1100 108 1162 110 L1162 640 L41 640 Z"/>
    <path class="main-field" fill="var(--card-purple)"
      d="M41 150 C150 140 230 170 330 172 C440 174 520 138 640 136 C760 134 840 168 940 166 C1040 164 1100 150 1162 152
         L1162 592 C1080 590 980 600 880 610 C760 622 640 580 540 598 C440 616 350 620 250 600 C160 582 90 580 41 590 Z"/>
    <path class="bottom-wave" fill="var(--wave-purple)"
      d="M41 590 C90 580 160 582 250 600 C350 620 440 616 540 598 C640 580 760 622 880 610 C980 600 1080 590 1162 592
         L1162 620 C1080 618 980 630 880 640 C760 652 640 610 540 628 C440 646 350 650 250 630 C160 612 90 606 41 616 Z"/>
  </svg>

  <div class="puppy-photo" role="img" aria-label="Photo of two fawn bullmastiff puppies lying on a dark blanket with pink paw prints"></div>

  <h1 class="kennel-name"><span class="first">Kestamor</span> <span class="second">Bullmastiffs</span></h1>
  <p class="web-address">www.Kestamor Bullmastiffs.com</p>
</div>
</body>
</html>
```